Web, logo, and business card Design

We are opening a cocktail/Cork Den which serves tapas. It's outdoors surrounded by an old heritage listed building 'Elder Colonial Lodge' in the midst of a park. The bar will be full of ambience with an industrial feel but also fun, young and fresh, not old and stuffy. Fairy lights, old barrels, big colourful couches and high tables will mostly make up the decor along with candles, plants and building uplighting. We will offer 3 private rooms for small functions, the only indoor areas available. Fireplaces and heaters will be everywhere during an Aussie winter and umbrellas for those hot days. The establishment is named 'Cork Den'. We are after a logo design, web design and business card design to suit the style of our establishment.

Target Market(s)

Young professionals, couples and groups

Contact Information for Business Card

Name: Cork Den
Address: Elder Colonial Lodge
Wendlow Reserve
Wendlow NSW 2163 (enter the park from Quarrel St)

1km from the new Wendlow Arena and Wendlow Station

Website: corkdenhaven.example.au
Email: info@corkdenhaven.example
facebook: Cork Den Haven
Instagram: Cork Den Haven

Logo Text

Cork Den

Coding

Coded - Design and coding required

Number of Pages Required

1 page

Colors

Designer to choose colors to be used in the design.

Requirements
Must have
• Must have a home page and a click through to food Menu, drink menu (which we are still working on)
• Must be able to enquire and send emails easily from website.
• I must be able to update myself easily should anything change
• There's a basic temporary site available which you will be replacing, feel free to have a look.
• Looking for fun, sexy, fresh, ambience. The venue is a historic one.
Nice to have
• Map, reservations tab, a little info about Elder Colonial lodge. There's some already on the current site which you can use. Music perhaps?

```html
<!DOCTYPE html>
<html lang="en">
<head>
<meta charset="utf-8">
<title>Cork Den — Business Card</title>
<link rel="stylesheet" href="https://fonts.googleapis.com/css2?family=Oswald:wght@500;600&family=Arimo:wght@400&display=swap">
<style>
  :root {
    --stage: #0b0a0c;
    --card-light: #f6f7f9;
    --brand-red: #fe0000;
    --accent-red: #ef1c1c;
    --ink: #1c1c1c;
    --white: #ffffff;
  }
  html, body {
    margin: 0;
    padding: 0;
    width: 1200px;
    height: 1200px;
    overflow: hidden;
    background: var(--stage);
  }
  .stage {
    position: relative;
    width: 1200px;
    height: 1200px;
    background: var(--stage);
  }
  .card {
    position: absolute;
    width: 874px;
    height: 498px;
  }
  .card--front {
    left: 169px;
    top: 88px;
    background: var(--card-light);
  }
  .card--back {
    left: 164px;
    top: 637px;
    background: var(--brand-red);
  }
  .wordmark {
    position: absolute;
    font-family: "Oswald", sans-serif;
    font-weight: 500;
    text-transform: uppercase;
    line-height: 0.95;
    letter-spacing: 2px;
    text-align: right;
  }
  .card--front .wordmark {
    left: 48px;
    top: 210px;
    width: 170px;
    font-size: 50px;
    color: var(--ink);
  }
  .card--back .wordmark {
    left: 352px;
    top: 190px;
    width: 170px;
    font-size: 50px;
    color: var(--white);
  }
  .divider {
    position: absolute;
    left: 332px;
    top: 153px;
    width: 4px;
    height: 312px;
    background: var(--accent-red);
  }
  .person-name {
    position: absolute;
    left: 424px;
    top: 142px;
    margin: 0;
    font-family: "Oswald", sans-serif;
    font-weight: 600;
    font-size: 48px;
    line-height: 1;
    letter-spacing: 0.5px;
    color: var(--accent-red);
    transform: scaleY(1.08);
    transform-origin: left top;
  }
  .person-role {
    position: absolute;
    left: 424px;
    top: 202px;
    margin: 0;
    font-family: "Arimo", sans-serif;
    font-size: 25px;
    line-height: 1;
    letter-spacing: 3.4px;
    color: var(--accent-red);
  }
  .contact-list {
    position: absolute;
    left: 432px;
    top: 260px;
    margin: 0;
    padding: 0;
    list-style: none;
  }
  .contact-item {
    display: flex;
    align-items: center;
    height: 38px;
    margin-bottom: 15px;
    font-family: "Arimo", sans-serif;
    font-size: 18px;
    color: var(--ink);
  }
  .contact-item svg {
    width: 38px;
    height: 38px;
    margin-right: 35px;
    flex: none;
  }
</style>
</head>
<body>
<main class="stage">
  <section class="card card--front" aria-label="Business card front">
    <div class="wordmark">Cork<br>Den</div>
    <div class="divider"></div>
    <h1 class="person-name">NAME OF PERSON</h1>
    <p class="person-role">GENERAL MANAGER</p>
    <ul class="contact-list">
      <li class="contact-item">
        <svg viewBox="0 0 38 38" aria-hidden="true"><circle cx="19" cy="19" r="19" fill="#ef1c1c"/><rect x="11" y="13" width="16" height="12" fill="none" stroke="#fff" stroke-width="1.8"/><path d="M11 13 L19 20 L27 13" fill="none" stroke="#fff" stroke-width="1.8"/></svg>
        contact@corkden.example
      </li>
      <li class="contact-item">
        <svg viewBox="0 0 38 38" aria-hidden="true"><circle cx="19" cy="19" r="19" fill="#ef1c1c"/><path d="M13 11 l4 0 l1.5 4.5 l-2.5 1.8 a10 10 0 0 0 5 5 l1.8 -2.5 l4.5 1.5 l0 4 a2 2 0 0 1 -2 2 a15 15 0 0 1 -14 -14 a2 2 0 0 1 1.7 -2.3z" fill="#ffb3c6"/></svg>
        +0061 555 012 345
      </li>
      <li class="contact-item">
        <svg viewBox="0 0 38 38" aria-hidden="true"><circle cx="19" cy="19" r="19" fill="#ef1c1c"/><path d="M19 10 a6 6 0 0 1 6 6 c0 4.5 -6 11 -6 11 s-6 -6.5 -6 -11 a6 6 0 0 1 6 -6z" fill="none" stroke="#ffb3c6" stroke-width="1.8"/><circle cx="19" cy="16" r="2" fill="#ffb3c6"/></svg>
        Address Address Address
      </li>
      <li class="contact-item">
        <svg viewBox="0 0 38 38" aria-hidden="true"><circle cx="19" cy="19" r="19" fill="#ef1c1c"/><circle cx="19" cy="19" r="9" fill="none" stroke="#ffb3c6" stroke-width="1.8"/><path d="M10 19 h18 M19 10 c-4 5 -4 13 0 18 M19 10 c4 5 4 13 0 18" fill="none" stroke="#ffb3c6" stroke-width="1.5"/></svg>
        www.corkden.example
      </li>
    </ul>
  </section>

  <section class="card card--back" aria-label="Business card back">
    <div class="wordmark">Cork<br>Den</div>
  </section>
</main>
</body>
</html>
```